Tendril Harbor

Our product is a subscription-based website for doctors and medical practices. It allows contract-based doctors (locums) to book jobs with medical practices and to organise their own finances (invoicing, pension, etc). Also, it allows medical practices to post jobs, and book locums.

We need a website design that looks clean and professional. It should look easy-to-use and friendly, which will encourage users to sign up as they'll hopefully think using the system will also be simple and friendly.

As well as the homepage, we need a design for the logged-in view. This is very different to the website but equally important. It needs to be very functional. Much more like an application and less like a website.

PLEASE SUBMIT BOTH WEBSITE HOMEPAGE DESIGN AND APPLICATION DASHBOARD DESIGN.

The application is built and we already have a user interface (linked below) so we're not looking for a designer to decide what is on these pages - we already have that. We're ONLY asking for visual design. Please just make the content we have look good. You may move parts of the content around a small amount but the functionality is very much signed off now so it's only visual styling that we need addressed.

Please base the branding around the current logo, which can't be changed. You can get the logo as an EPS here : http://clients.brassowl.co.uk/tendrilharbor/design/logo-green.eps

Here is a link to the current design for the website, and for the application dashboard:
http://clients.brassowl.co.uk/tendrilharbor/design/

Also, here is a video we've had made which might help you with the brand:
http://quivlo.com/71825364
Updates

Just in case it isn't clear, the video (linked in the main brief) is an essential part of the website homepage.

Reason: We need to spend some time looking over these designs and might ask for a few amendments to one or two in the next few days. Thanks.

Target Market(s)

Doctors and medical practices

Industry/Entity Type

Medical

Requirements
Must have
• It must have all the features that are in the linked designs - homepage and dashboard.

```html
<!DOCTYPE html>
<html lang="en">
<head>
<meta charset="utf-8">
<title>Tendril Harbor – Dashboard</title>
<link href="https://fonts.googleapis.com/css2?family=Arimo:wght@400;700&display=swap" rel="stylesheet">
<style>
:root{
  --brand-blue:#1d6fa5;
  --brand-green:#7ab648;
  --header-top:#e9f6fd;
  --header-bottom:#f4fbf3;
  --header-line:#1d6fa5;
  --side-bg:#e3f1b5;
  --side-active:#6fb03e;
  --badge:#f39a1e;
  --text:#222;
  --muted:#555;
  --link:#1f73b7;
  --panel-border:#dcdcdc;
  --panel-head-top:#fafafa;
  --panel-head-bottom:#e6e6e6;
  --row-bg:#eeeeee;
  --row-strong:#d6d6d6;
  --busy:#cc4a45;
  --partial:#f0a23d;
  --free:#6aab4c;
  --btn-top:#2a95d6;
  --btn-bottom:#0f6aab;
  --feedback:#2e6f99;
}
*{box-sizing:border-box;margin:0;padding:0}
html,body{width:1200px;height:1142px;overflow:hidden}
body{font-family:"Arimo",Arial,sans-serif;color:var(--text);background:#fff;position:relative;font-size:12px}
a{color:var(--link);text-decoration:none}

.top-bar{position:absolute;left:0;top:0;width:1200px;height:91px;border-top:4px solid var(--header-line);
  background:linear-gradient(var(--header-top),var(--header-bottom));border-bottom:1px solid #cfe3c4}
.brand{position:absolute;left:42px;top:22px;display:flex;align-items:center;gap:12px}
.brand-dot{width:48px;height:48px;border-radius:50%;background:var(--brand-blue)}
.brand-name{font-size:24px;font-weight:700;color:var(--brand-blue);line-height:1}
.account{position:absolute;left:972px;top:20px}
.account-name{font-size:15px;font-weight:700;color:#333}
.account-links{margin-top:14px;display:flex;gap:12px;font-size:11.5px}
.account-links a{color:#333}

.sidebar{position:absolute;left:38px;top:94px;width:151px;height:1048px;background:var(--side-bg);border-right:1px solid #cbdc98}
.side-item{display:block;padding:0 10px;height:26px;line-height:26px;font-size:14px;font-weight:700;color:#333;border-bottom:1px solid #fff}
.side-item.active{background:var(--side-active);color:#fff;display:flex;justify-content:space-between;align-items:center}
.badge{background:var(--badge);color:#fff;font-size:11px;width:16px;height:16px;line-height:16px;text-align:center}
.side-group{border-bottom:1px solid #fff;padding:4px 0 6px}
.side-group .side-item{border:0;height:20px;line-height:20px}
.side-sub{display:block;padding:0 10px;font-size:11px;line-height:20.5px;color:#333}

.page-title{position:absolute;left:212px;top:112px;font-size:19px;font-weight:400;color:#222}
.get-started{position:absolute;left:1026px;top:107px;width:136px;height:34px;border-radius:17px;
  background:linear-gradient(var(--btn-top),var(--btn-bottom));color:#fff;font-weight:700;font-size:14px;
  display:flex;align-items:center;justify-content:center;gap:8px}
.get-started svg{width:13px;height:13px}

.panel-head{position:absolute;height:40px;border:1px solid var(--panel-border);border-radius:3px;
  background:linear-gradient(var(--panel-head-top),var(--panel-head-bottom));
  font-size:14px;font-weight:700;color:#333;padding:0 13px;display:flex;align-items:center;justify-content:space-between}
.panel-body{position:absolute;border:1px solid var(--panel-border);border-radius:3px;background:#fff}
.col-left{left:212px;width:432px}
.col-right{left:731px;width:432px}

.notice{padding:10px 12px;font-size:12.5px;position:relative;height:100%}
.notice-dot{display:inline-block;width:7px;height:7px;border-radius:50%;background:#d33;margin-right:5px;vertical-align:1px}
.notice-close{position:absolute;right:10px;top:6px;width:16px;height:16px;border:1px solid #bbb;background:#eee;font-size:10px;text-align:center;line-height:14px}
.see-all{position:absolute;right:10px;bottom:9px;font-size:11.5px}

.cal-nav{display:flex;justify-content:space-between;align-items:center;margin:9px 10px 0}
.cal-btn{width:58px;height:28px;border:1px solid #ccc;background:linear-gradient(#fafafa,#e4e4e4);border-radius:2px;text-align:center;line-height:27px;font-size:13px}
.cal-month{font-size:14px;font-weight:700}
.cal-grid{margin:8px 10px 0;display:grid;grid-template-columns:repeat(7,58px);grid-auto-rows:34px}
.cal-dow{height:22px;text-align:center;font-size:11.5px;font-weight:700;line-height:18px}
.day{border:1px solid #e2e2e2;display:flex;align-items:center;justify-content:center}
.day span{width:52px;height:28px;border-radius:2px;color:#fff;font-weight:700;font-size:13px;display:flex;align-items:center;justify-content:center;position:relative}
.busy span{background:var(--busy);border:1px solid #a93a36}
.partial span{background:var(--partial);border:1px solid #d2872a}
.free span{background:var(--free);border:1px solid #528c3a}
.tooltip{position:absolute;left:397px;top:448px;width:180px;height:51px;background:#111;border:1px solid #666;color:#eee;font-size:11.5px;line-height:17px;padding:7px 13px}
.tooltip::after{content:"";position:absolute;left:84px;bottom:-8px;border:8px solid transparent;border-bottom:0;border-top-color:#111}
.cursor{position:absolute;left:486px;top:517px;width:12px;height:17px}
.legend{display:flex;gap:16px;margin:18px 10px 0;font-size:11.5px;align-items:center}
.legend i{display:inline-block;width:22px;height:14px;border-radius:2px;vertical-align:-3px;margin-right:5px}
.see-appts{position:absolute;right:10px;bottom:11px;font-size:11.5px}

.stat-list{padding:4px 4px}
.stat-row{display:flex;height:33px;margin:4px 0;align-items:center;background:var(--row-bg);padding:0 12px;font-size:12.5px}
.stat-row .label{flex:1}
.stat-row .value{width:74px}
.stat-row.strong{background:var(--row-strong);font-weight:700}
.right-stat .value{width:auto}

.job{display:flex;padding:11px 12px;font-size:11.5px;line-height:17px}
.job-addr{width:164px}
.job-addr b{font-size:12px}
.job-date{font-size:12px;margin-bottom:4px}
.job-links{border:1px solid #cfdde8;padding:2px 10px 1px;font-size:12px;width:243px}
.job-links div::before{content:"▸ ";font-size:9px;color:#333}

.map{position:absolute;left:3px;top:3px;width:424px;height:224px;background:linear-gradient(135deg,#e8e3c8,#dfe6c9 45%,#d6dcc2 70%,#c5d4de)}
.map-toggle{position:absolute;right:6px;top:6px;display:flex;font-size:12px;background:#fff;border:1px solid #aaa}
.map-toggle span{padding:2px 7px}
.map-toggle b{padding:2px 7px;border-right:1px solid #aaa}
.map-table{position:absolute;left:6px;top:228px;width:420px;font-size:11.5px}
.map-head,.map-row{display:grid;grid-template-columns:190px 1fr 90px;align-items:center}
.map-head{font-weight:700;height:20px;padding-left:6px}
.map-row{height:18px}
.map-row .name::before{content:"";display:inline-block;width:13px;height:13px;border-radius:50%;background:#b8332f;margin-right:5px;vertical-align:-2px}
.r{text-align:right}

.radios{display:flex;gap:14px;font-size:12px;font-weight:400}
.radios i{display:inline-block;width:12px;height:12px;border:1px solid #888;border-radius:50%;background:#fff;vertical-align:-2px;margin-right:5px;position:relative}
.radios i.on::after{content:"";position:absolute;left:2px;top:2px;width:6px;height:6px;border-radius:50%;background:var(--brand-blue)}

.feedback{position:absolute;left:974px;top:1115px;width:188px;height:30px;background:var(--feedback);border-radius:3px 3px 0 0;color:#fff;font-size:14px;display:flex;align-items:center;justify-content:center;gap:8px}
.feedback svg{width:20px;height:14px}
</style>
</head>
<body>

<header class="top-bar">
  <div class="brand"><span class="brand-dot"></span><span class="brand-name">Tendril Harbor</span></div>
  <div class="account">
    <div class="account-name">Mrs. Helen Marsdale</div>
    <nav class="account-links"><a href="#">Profile</a><a href="#">Settings</a><a href="#">Referal</a><a href="#">Sign out</a></nav>
  </div>
</header>

<nav class="sidebar">
  <a class="side-item active" href="#">Dashboard <span class="badge">1</span></a>
  <a class="side-item" href="#">Profile</a>
  <a class="side-item" href="#">Diary</a>
  <div class="side-group"><a class="side-item" href="#">My Jobs</a><a class="side-sub" href="#">Find a job</a></div>
  <div class="side-group"><a class="side-item" href="#">My Finances</a><a class="side-sub" href="#">Invoices</a><a class="side-sub" href="#">Pensions</a><a class="side-sub" href="#">Expenses</a><a class="side-sub" href="#">Income/Expenses report</a></div>
  <div class="side-group"><a class="side-item" href="#">My Network</a><a class="side-sub" href="#">Search employers</a><a class="side-sub" href="#">Invite employers</a></div>
</nav>

<h1 class="page-title">Dashboard</h1>
<a class="get-started" href="#">Get Started <svg viewBox="0 0 14 14"><circle cx="7" cy="7" r="6" fill="none" stroke="#fff" stroke-width="1.4"/><path d="M6 4l3 3-3 3" fill="none" stroke="#fff" stroke-width="1.4"/></svg></a>

<!-- Left column -->
<div class="panel-head col-left" style="top:158px">Notifications</div>
<div class="panel-body col-left" style="top:206px;height:57px">
  <div class="notice"><span class="notice-dot"></span><a href="#">Mill Lane Surgery has posted a new job.</a>
    <span class="notice-close">x</span><a class="see-all" href="#">See all ➔</a></div>
</div>

<div class="panel-head col-left" style="top:282px">My dairy</div>
<div class="panel-body col-left" style="top:331px;height:305px">
  <div class="cal-nav"><span class="cal-btn">&lt;</span><span class="cal-month">January 2013</span><span class="cal-btn">&gt;</span></div>
  <div class="cal-grid">
    <div class="cal-dow">Mon</div><div class="cal-dow">Tue</div><div class="cal-dow">Wed</div><div class="cal-dow">Thu</div><div class="cal-dow">Fri</div><div class="cal-dow">Sat</div><div class="cal-dow">Sun</div>
    <div class="day"></div><div class="day free"><span>1</span></div><div class="day free"><span>2</span></div><div class="day partial"><span>3</span></div><div class="day free"><span>4</span></div><div class="day free"><span>5</span></div><div class="day free"><span>6</span></div>
    <div class="day free"><span>7</span></div><div class="day busy"><span>8</span></div><div class="day busy"><span>9</span></div><div class="day busy"><span>10</span></div><div class="day free"><span>11</span></div><div class="day free"><span>12</span></div><div class="day free"><span>13</span></div>
    <div class="day busy"><span>14</span></div><div class="day busy"><span>15</span></div><div class="day free"><span>16</span></div><div class="day free"><span>17</span></div><div class="day free"><span>18</span></div><div class="day free"><span>19</span></div><div class="day free"><span>20</span></div>
    <div class="day free"><span>21</span></div><div class="day partial"><span>22</span></div><div class="day partial"><span>23</span></div><div class="day partial"><span>24</span></div><div class="day partial"><span>25</span></div><div class="day free"><span>26</span></div><div class="day free"><span>27</span></div>
    <div class="day free"><span>28</span></div><div class="day free"><span>29</span></div><div class="day busy"><span>30</span></div><div class="day busy"><span>31</span></div><div class="day"></div><div class="day"></div><div class="day"></div>
  </div>
  <div class="legend"><span><i style="background:var(--busy)"></i>Busy</span><span><i style="background:var(--partial)"></i>Partially available</span><span><i style="background:var(--free)"></i>Available</span></div>
  <a class="see-appts" href="#">See all appointments</a>
</div>
<div class="tooltip">Brookfield Medical Centre:<br>08:00 - 12:00</div>
<svg class="cursor" viewBox="0 0 12 17"><path d="M1 1v13l3-3 2 5 2-1-2-5h4z" fill="#fff" stroke="#000"/></svg>

<div class="panel-head col-left" style="top:654px">My jobs</div>
<div class="panel-body col-left" style="top:702px;height:190px">
  <div class="stat-list">
    <div class="stat-row"><span class="label">Jobs booked</span><span class="value">17</span></div>
    <div class="stat-row"><span class="label">Jobs requiring confirmation</span><span class="value">0</span></div>
    <div class="stat-row strong"><span class="label">Pending applications</span><span class="value">2</span></div>
    <div class="stat-row"><span class="label">Jobs invited</span><span class="value">1</span></div>
    <div class="stat-row"><span class="label">My network</span><span class="value">9</span></div>
  </div>
</div>

<!-- Right column -->
<div class="panel-head col-right" style="top:158px">Current or next job</div>
<div class="panel-body col-right" style="top:206px;height:89px">
  <div class="job"><div class="job-addr"><b>Ashgrove Surgery</b><br>42 Elm Street,<br>London<br>N4 2RT</div>
    <div><div class="job-date">17 Jan 2012 - 21 Jan 2013 (9:30 - 16:00)</div>
      <div class="job-links"><div><a href="#">Earnings from this employer: £23,887</a></div><div><a href="#">This surgery has 8 unfilled jobs.</a></div></div></div></div>
</div>

<div class="panel-head col-right" style="top:314px">Following</div>
<div class="panel-body col-right" style="top:361px;height:89px">
  <div class="job"><div class="job-addr"><b>Dr Verma Surgery</b><br>8 Ferncliff Avenue,<br>London<br>NW6 4QP</div>
    <div><div class="job-date">23 Jan 2012 (9:30 - 15:30)</div>
      <div class="job-links"><div><a href="#">Earnings from this employer: £652</a></div><div>This surgery has 8 unfilled jobs.</div></div></div></div>
</div>

<div class="panel-head col-right" style="top:469px">Jobs within 20 miles</div>
<div class="panel-body col-right" style="top:517px;height:291px">
  <div class="map" role="img" aria-label="Road map of London and surrounding towns with two employer pins near central London">
    <div class="map-toggle"><b>Map</b><span>Satellite</span></div>
  </div>
  <div class="map-table">
    <div class="map-head"><span>Employer name</span><span>Jobs available</span><span class="r">Distance</span></div>
    <div class="map-row"><a class="name" href="#">Willow Tree Surgery</a><a href="#">14</a><span class="r">0.8 miles</span></div>
    <div class="map-row"><a class="name" href="#">Mill Lane Surgery</a><span>0</span><span class="r">2.73 miles</span></div>
  </div>
</div>

<div class="panel-head col-right" style="top:830px">Financial summery
  <span class="radios"><span><i class="on"></i>Tax year</span><span><i></i>Current year</span></span></div>
<div class="panel-body col-right" style="top:877px;height:191px">
  <div class="stat-list right-stat">
    <div class="stat-row"><span class="label">Paid invoices</span><span class="value">£53,769</span></div>
    <div class="stat-row"><span class="label">Unpaid invoices</span><span class="value">£3,188</span></div>
    <div class="stat-row strong"><span class="label">Total earned</span><span class="value">£56,976</span></div>
    <div class="stat-row"><span class="label">Pension claimed</span><span class="value">£5,238</span></div>
    <div class="stat-row"><span class="label">Expenses</span><span class="value">£2,143</span></div>
  </div>
</div>

<a class="feedback" href="#"><svg viewBox="0 0 20 14"><path d="M2 4h4l8-3v12l-8-3H2z" fill="none" stroke="#fff" stroke-width="1.4"/><path d="M5 10l1 3" stroke="#fff" stroke-width="1.4"/></svg>Feedback &amp; Support</a>

</body>
</html>
```